I want a double sided flyer possibly with a picture of a lawn or grass.
Company name, phone number, email, and logo
Halvorsen Turf Management, (404)726-1853,Halvorsen_Turf@brevimail.com
Company services
Fertilization and weed control,Lawn and Landscape maintenance, mowing, pruning, aeration, landscape and Christmas lights,

```html
<!DOCTYPE html>
<html lang="en">
<head>
<meta charset="utf-8">
<title>Halvorsen Turf Management – Flyer</title>
<link href="https://fonts.googleapis.com/css2?family=Oswald:wght@500;700&family=Roboto+Slab:wght@400;700&display=swap" rel="stylesheet">
<style>
  :root {
    --green-deep: #0d5a1f;
    --green-mid: #18772a;
    --green-bright: #3fae49;
    --yellow: #e3cf12;
    --white: #ffffff;
    --rule: rgba(255,255,255,0.5);
  }
  * { margin: 0; padding: 0; box-sizing: border-box; }
  html, body { width: 1200px; height: 603px; overflow: hidden; background: var(--white); }
  .flyer { position: relative; width: 1200px; height: 603px; overflow: hidden; }

  .panel { position: absolute; top: 0; height: 603px; overflow: hidden; }
  .panel-back { left: 0; width: 600px; background: var(--white); }
  .panel-front { left: 600px; width: 600px; }

  .photo { position: absolute; }
  .photo-edging { left: 0; top: 0; width: 361px; height: 218px;
    background:
      radial-gradient(ellipse 45% 55% at 82% 70%, #d9cfb6 0%, rgba(217,207,182,0) 100%),
      radial-gradient(ellipse 40% 40% at 65% 18%, #e2c23a 0%, rgba(226,194,58,0) 70%),
      radial-gradient(ellipse 55% 50% at 20% 85%, #9cc24e 0%, rgba(156,194,78,0) 100%),
      linear-gradient(180deg, #24381a 0%, #4e6e2c 45%, #7fa448 100%); }
  .photo-hedge { left: 367px; top: 0; width: 233px; height: 152px;
    background:
      radial-gradient(ellipse 30% 60% at 8% 30%, #5a5f66 0%, rgba(90,95,102,0) 100%),
      radial-gradient(ellipse 30% 25% at 85% 38%, #b89a66 0%, rgba(184,154,102,0) 100%),
      linear-gradient(180deg, #2c3f22 0%, #3d6a22 38%, #7ab93a 62%, #5f9c2c 100%); }
  .accent-box { position: absolute; left: 367px; top: 158px; width: 233px; height: 60px; background: var(--green-bright); }
  .photo-garden { left: 0; top: 224px; width: 600px; height: 140px;
    background:
      radial-gradient(ellipse 22% 40% at 30% 18%, #e7e2d6 0%, rgba(231,226,214,0) 100%),
      radial-gradient(ellipse 18% 30% at 58% 72%, #e04f9c 0%, rgba(224,79,156,0) 100%),
      radial-gradient(ellipse 14% 25% at 86% 35%, #6d5fc4 0%, rgba(109,95,196,0) 100%),
      radial-gradient(ellipse 14% 25% at 12% 20%, #e06a2a 0%, rgba(224,106,42,0) 100%),
      linear-gradient(180deg, #4d6b34 0%, #3f7d2e 45%, #6fb53a 80%, #5aa52f 100%); }

  .back-curve { position: absolute; left: 0; top: 290px; width: 600px; height: 313px; }

  .services { position: absolute; left: 0; top: 385px; width: 600px; text-align: center; color: var(--yellow);
    font-family: 'Roboto Slab', serif; }
  .services-title { display: flex; align-items: center; justify-content: center; gap: 12px;
    font-weight: 700; font-size: 21px; line-height: 28px; }
  .services-title::before, .services-title::after { content: ""; width: 50px; height: 1px; background: var(--yellow); opacity: .7; }
  .services-list { margin: 1px auto 0; width: 500px; font-size: 18px; line-height: 25px; }

  .divider { position: absolute; left: 56px; top: 497px; width: 472px; border-top: 1px dashed var(--rule); }

  .contact { position: absolute; left: 0; top: 512px; width: 600px; text-align: center; color: var(--white);
    font-family: 'Roboto Slab', serif; }
  .contact-email { font-size: 18px; line-height: 24px; }
  .contact-phone { font-size: 37px; font-weight: 700; line-height: 44px; }

  .photo-mowing { left: 0; top: 0; width: 600px; height: 603px;
    background:
      radial-gradient(ellipse 35% 45% at 72% 48%, #3f7a2a 0%, rgba(63,122,42,0) 100%),
      radial-gradient(ellipse 40% 40% at 40% 62%, #8fd14a 0%, rgba(143,209,74,0) 100%),
      radial-gradient(ellipse 30% 60% at 5% 45%, #1f3d16 0%, rgba(31,61,22,0) 100%),
      linear-gradient(180deg, #1f3a18 0%, #2f5a22 18%, #5fae34 36%, #7cc442 60%, #55a02e 100%); }
  .front-curve { position: absolute; left: 0; top: 470px; width: 600px; height: 133px; }

  .brand { position: absolute; left: 95px; top: 40px; width: 180px; text-align: center; color: var(--white); }
  .brand-dot { width: 66px; height: 66px; border-radius: 50%; background: var(--white); margin: 0 auto 14px; }
  .brand-name { font-family: 'Oswald', sans-serif; font-weight: 500; font-size: 24px; line-height: 28px; letter-spacing: .5px; }

  .headline { position: absolute; left: 0; top: 532px; width: 600px; text-align: center;
    font-family: 'Oswald', sans-serif; font-weight: 700; font-size: 41px; line-height: 52px; color: var(--white); }
  .headline .first { color: var(--yellow); }
</style>
</head>
<body>
<main class="flyer">
  <section class="panel panel-back">
    <div class="photo photo-edging" role="img" aria-label="Gloved hand trimming grass edge with hand shears"></div>
    <div class="photo photo-hedge" role="img" aria-label="Gardener trimming a hedge with a power trimmer"></div>
    <div class="accent-box"></div>
    <div class="photo photo-garden" role="img" aria-label="Landscaped front yard with flower beds and lawn"></div>

    <svg class="back-curve" viewBox="0 0 600 313" preserveAspectRatio="none" aria-hidden="true">
      <path d="M0 18 Q200 85 600 22 L600 313 L0 313 Z" fill="var(--yellow)"/>
      <path d="M0 40 Q210 100 600 42 L600 313 L0 313 Z" fill="var(--green-mid)"/>
      <path d="M0 150 Q300 120 600 110 L600 313 L0 313 Z" fill="var(--green-deep)" opacity=".45"/>
    </svg>

    <div class="services">
      <h2 class="services-title">Company services</h2>
      <p class="services-list">Fertilization and weed control, Lawn and Landscape Maintenance, Mowing, Pruning, Aeration, Landscape and Christmas lights.</p>
    </div>
    <div class="divider"></div>
    <div class="contact">
      <p class="contact-email">Halvorsen_Turf@brevimail.com</p>
      <p class="contact-phone">PH: (404)726-1853</p>
    </div>
  </section>

  <section class="panel panel-front">
    <div class="photo photo-mowing" role="img" aria-label="Worker mowing a green lawn on a ride-on mower, grass clippings flying"></div>

    <div class="brand">
      <div class="brand-dot"></div>
      <p class="brand-name">Halvorsen Turf Management</p>
    </div>

    <svg class="front-curve" viewBox="0 0 600 133" preserveAspectRatio="none" aria-hidden="true">
      <path d="M0 8 Q300 60 600 18 L600 133 L0 133 Z" fill="var(--white)"/>
      <path d="M0 16 Q300 66 600 28 L600 133 L0 133 Z" fill="var(--green-mid)"/>
    </svg>

    <h1 class="headline"><span class="first">HALVORSEN</span> TURF MANAGEMENT.</h1>
  </section>
</main>
</body>
</html>
```